Business Card for Yachting Management Company

Need a business card design for a new yachting project management company. Attached is the logo for the company.
Our clients are large yacht owners and captains.
Design must be in the style of the logo. Modern, elegant.

Example of data to show:
Peter Hollis
Project Manager
(+34) 612 738 104
peter@quorvane.net
Quorvane Management - Meridel Tower, Office 22 - KRB - Palma de Mallorca

The data above will have to be changed (by me) for the different people in the company over the next years.

Will be printed using PrintNova (Lustre Card Series). They provide these guidelines for the size:
"the actual size of the card is 1050 x 600 pixels. However, the full bleed size is 1083 x 633 pixels, and the safe printing area is 1008 x 558 pixels."

```html
<!DOCTYPE html>
<html lang="en">
<head>
<meta charset="UTF-8">
<title>Quorvane Management – Business Card</title>
<link rel="stylesheet" href="https://fonts.googleapis.com/css2?family=Montserrat:wght@400;500;600;700&display=swap">
<style>
  :root {
    --stage: #161616;
    --card: #242424;
    --card-back: #1d1d1d;
    --pattern-dark: #1b1b1b;
    --pattern-light: #2e2e2e;
    --blue: #1a82d6;
    --white: #f2f2f2;
  }
  * { box-sizing: border-box; margin: 0; padding: 0; }
  html, body {
    width: 1200px;
    height: 900px;
    overflow: hidden;
    background: var(--stage);
    font-family: "Montserrat", sans-serif;
  }
  .sheet {
    width: 1200px;
    height: 900px;
    display: flex;
    flex-direction: column;
    align-items: center;
    justify-content: center;
    gap: 40px;
  }
  .card {
    position: relative;
    width: 665px;
    height: 380px;
    overflow: hidden;
  }

  /* Back side */
  .card--back { background: var(--card-back); }
  .card__pattern {
    position: absolute;
    inset: 0;
    background: linear-gradient(115deg, var(--pattern-dark) 0%, var(--pattern-light) 55%, var(--pattern-dark) 100%);
  }
  .card__brand {
    position: absolute;
    left: 50%;
    top: 50%;
    transform: translate(-50%, -50%);
    text-align: center;
    color: var(--blue);
    font-weight: 600;
    letter-spacing: 0.22em;
    line-height: 1.3;
  }
  .card__brand-name { font-size: 40px; letter-spacing: 0.06em; }
  .card__brand-sub { font-size: 15px; }

  /* Front side */
  .card--front {
    background: var(--card);
    display: flex;
    align-items: center;
    padding: 0 46px 0 52px;
  }
  .front__brand {
    width: 265px;
    color: var(--blue);
    font-weight: 600;
    line-height: 1.2;
  }
  .front__brand-name { font-size: 44px; letter-spacing: 0.02em; }
  .front__brand-sub { font-size: 18px; letter-spacing: 0.3em; }
  .front__divider {
    width: 2px;
    height: 190px;
    background: var(--blue);
    margin: 0 26px 0 24px;
  }
  .front__details { color: var(--white); font-size: 14px; line-height: 1.4; }
  .person__name {
    color: var(--blue);
    font-weight: 700;
    font-size: 22px;
    letter-spacing: 0.06em;
    text-transform: uppercase;
  }
  .person__role { font-size: 15px; margin-bottom: 8px; }
  .company__name { color: var(--blue); font-size: 15px; }
  .company__address { margin-bottom: 8px; }
  .contact { list-style: none; }
  .contact__item { display: flex; align-items: center; gap: 8px; }
  .contact__icon { width: 11px; height: 11px; flex: none; }
</style>
</head>
<body>
<main class="sheet">
  <section class="card card--back" aria-label="Card back">
    <div class="card__pattern" role="img" aria-label="Subtle repeating tone-on-tone brand pattern"></div>
    <div class="card__brand">
      <div class="card__brand-name">QUORVANE</div>
      <div class="card__brand-sub">MANAGEMENT</div>
    </div>
  </section>

  <section class="card card--front" aria-label="Card front">
    <div class="front__brand">
      <div class="front__brand-name">Quorvane</div>
      <div class="front__brand-sub">MANAGEMENT</div>
    </div>
    <div class="front__divider"></div>
    <div class="front__details">
      <p class="person__name">Peter Hollis</p>
      <p class="person__role">Project Manager</p>
      <p class="company__name">Quorvane Management</p>
      <p class="company__address">Meridel Tower, Office<br>22 - KRB - Palma de Mallorca</p>
      <ul class="contact">
        <li class="contact__item">
          <svg class="contact__icon" viewBox="0 0 12 12" aria-hidden="true"><path d="M2.5 1 L4.5 1 L5 3.5 L3.8 4.5 Q5 7 7.5 8.2 L8.5 7 L11 7.5 L11 9.5 Q10.5 11 9 11 Q2 10 1 3 Q1 1.5 2.5 1 Z" fill="var(--blue)"/></svg>
          <span>(+34) 612 738 104</span>
        </li>
        <li class="contact__item">
          <svg class="contact__icon" viewBox="0 0 12 12" aria-hidden="true"><rect x="1" y="2.5" width="10" height="7" fill="none" stroke="var(--blue)" stroke-width="1.2"/><path d="M1 2.5 L6 6.5 L11 2.5" fill="none" stroke="var(--blue)" stroke-width="1.2"/></svg>
          <span>peter@quorvane.net</span>
        </li>
        <li class="contact__item">
          <svg class="contact__icon" viewBox="0 0 12 12" aria-hidden="true"><circle cx="6" cy="6" r="5" fill="none" stroke="var(--blue)" stroke-width="1.1"/><ellipse cx="6" cy="6" rx="2.2" ry="5" fill="none" stroke="var(--blue)" stroke-width="1"/><path d="M1 6 H11" stroke="var(--blue)" stroke-width="1"/></svg>
          <span>www.quorvanemanagement.net</span>
        </li>
      </ul>
    </div>
  </section>
</main>
</body>
</html>
```